Design for online reviews widget

Attached is a wireframe of a widget we need designing to display reviews on websites from multiple sources. We need this provided at 3 different sizes including full screen, contained (like the wireframe) and mobile.
You have completely free rein on the styling.
The only elements that should remain untouched are the blue stars (https://www.filquarry.net/s/8vtmwp2291zq4h/kv%20stars.ai?dl=0) and powered by logo at the bottom.
Ignore the menu at the top of the wireframe, this is just from the website the widget will be placed on.
Businesses

```html
<!DOCTYPE html>
<html lang="en">
<head>
<meta charset="utf-8">
<title>Reviews widget</title>
<link rel="stylesheet" href="https://fonts.googleapis.com/css2?family=Roboto:wght@400;500;700&family=Hind:wght@400;600;700&display=swap">
<style>
:root{
  --nav-bg:#272727;
  --nav-text:#ffffff;
  --nav-active:#56a838;
  --page-bg:#eeeff4;
  --panel-bg:#ffffff;
  --card-border:#e4e4e4;
  --card-highlight:#cfe6f7;
  --heading:#111111;
  --body:#4a4a4a;
  --meta-green:#4c9c2a;
  --sky:#35bdea;
  --gold:#f7b21b;
  --source-text:#2b2b2b;
  --badge-grey:#d9dde3;
}
*{box-sizing:border-box;margin:0;padding:0}
html,body{width:1200px;height:1200px;overflow:hidden}
body{background:var(--page-bg);font-family:"Hind",sans-serif;position:relative}
.site-nav{position:absolute;left:0;top:0;width:1200px;height:47px;background:var(--nav-bg);display:flex;justify-content:center;align-items:stretch;font-family:"Roboto",sans-serif;font-weight:500;font-size:13px;color:var(--nav-text);letter-spacing:.1px}
.site-nav span{display:flex;align-items:center;padding:0 15px}
.site-nav .active{background:var(--nav-active)}
.score{position:absolute;top:84px;left:0;width:1200px;text-align:center}
.score-stars{display:flex;justify-content:center;gap:6px}
.score-text{margin-top:10px;font-family:"Roboto",sans-serif;font-size:16px;color:#111}
.panel{position:absolute;left:111px;top:169px;width:976px;height:894px;background:var(--panel-bg);box-shadow:0 0 5px rgba(0,0,0,.18)}
.review{position:absolute;left:19px;width:936px;border:1px solid var(--card-border);box-shadow:0 0 3px rgba(0,0,0,.06)}
.review.featured{border-color:var(--card-highlight);box-shadow:0 0 4px rgba(53,189,234,.25)}
.review-body{position:absolute;left:11px;top:11px;width:752px}
.review-side{position:absolute;left:768px;top:8px;bottom:8px;right:0;border-left:1px solid #eee;display:flex;flex-direction:column;align-items:center;justify-content:center;gap:16px}
.review-title{font-weight:700;font-size:14.5px;color:var(--heading);line-height:18px;margin-bottom:2px}
.review-text{font-size:13.6px;color:var(--body);line-height:22.6px}
.review.featured .review-text{line-height:26px}
.review-scores,.review-service{font-size:13.6px;color:var(--heading);line-height:24px}
.review-scores b,.review-service b{font-weight:700}
.review-service{color:var(--body)}
.review-service b{color:var(--heading)}
.review-meta{font-size:13.6px;color:var(--meta-green);line-height:23px}
.source-name{font-family:"Hind",sans-serif;font-weight:600;font-size:26px;line-height:1;color:var(--source-text)}
.source-badge{width:92px;height:92px;border-radius:50%;background:var(--badge-grey)}
.stars{display:flex;gap:3px}
.load-more{position:absolute;left:427px;top:815px;width:124px;height:38px;background:var(--sky);color:#fff;font-family:"Roboto",sans-serif;font-weight:700;font-size:17px;border-radius:3px;display:flex;align-items:center;justify-content:center}
.powered{position:absolute;left:880px;top:1095px;width:190px}
.powered-label{font-family:"Roboto",sans-serif;font-size:15px;color:#111;text-align:center;margin-left:30px}
.powered-brand{display:flex;align-items:center;gap:6px;margin-top:6px;font-family:"Roboto",sans-serif;font-weight:700;font-size:22px;color:#1a1a1a}
.powered-brand i{width:44px;height:44px;border-radius:50%;background:var(--sky);display:block}
</style>
</head>
<body>
<svg width="0" height="0" style="position:absolute">
  <defs>
    <symbol id="star" viewBox="0 0 24 24"><path d="M12 1.5l3.1 6.9 7.4.7-5.6 5 1.7 7.4L12 17.7 5.4 21.5l1.7-7.4-5.6-5 7.4-.7z"/></symbol>
  </defs>
</svg>

<nav class="site-nav">
  <span>HOME</span><span>ABOUT ▼</span><span>WINDOWS ▼</span><span>DOORS ▼</span><span>ORANGERIES &amp; EXTENSIONS ▼</span><span>ROOFS ▼</span><span>OUR WORK ▼</span><span class="active">REVIEWS ▼</span><span>BLOG</span><span>CONTACT</span>
</nav>

<section class="score">
  <div class="score-stars">
    <svg width="37" height="37" viewBox="0 0 37 37"><circle cx="18.5" cy="18.5" r="18.5" fill="var(--sky)"/><use href="#star" x="7" y="7" width="23" height="23" fill="#fff"/></svg>
    <svg width="37" height="37" viewBox="0 0 37 37"><circle cx="18.5" cy="18.5" r="18.5" fill="var(--sky)"/><use href="#star" x="7" y="7" width="23" height="23" fill="#fff"/></svg>
    <svg width="37" height="37" viewBox="0 0 37 37"><circle cx="18.5" cy="18.5" r="18.5" fill="var(--sky)"/><use href="#star" x="7" y="7" width="23" height="23" fill="#fff"/></svg>
    <svg width="37" height="37" viewBox="0 0 37 37"><circle cx="18.5" cy="18.5" r="18.5" fill="var(--sky)"/><use href="#star" x="7" y="7" width="23" height="23" fill="#fff"/></svg>
    <svg width="37" height="37" viewBox="0 0 37 37"><circle cx="18.5" cy="18.5" r="18.5" fill="var(--sky)"/><use href="#star" x="7" y="7" width="23" height="23" fill="#fff"/></svg>
  </div>
  <p class="score-text">Combined Review Score 4.3 out of 5</p>
</section>

<main class="panel">
  <article class="review featured" style="top:17px;height:175px">
    <div class="review-body">
      <h3 class="review-title">Front door with windows each side and side window</h3>
      <p class="review-text">This is the second time we have used regent home Upgrades , and the service is amazing! Nolan came round several times as we keep changing our minds and he was so helpful and gave us good advice, and the guys who do the fitting are efficient and tidy . I've got to say the end result is amazing and I have recommended to many of friends . Thanks Regent</p>
      <p class="review-scores"><b>Reliablity:</b> 9.38 <b>Courtesy:</b> 10 <b>Tidiness:</b> 9.84 <b>Workmanship:</b> 10</p>
      <p class="review-meta">Verified 28th September 2021 | Located in Elmbridge</p>
    </div>
    <div class="review-side" style="gap:14px">
      <div class="source-name">Tradesmark</div>
      <div class="source-badge"></div>
    </div>
  </article>

  <article class="review" style="top:220px;height:175px">
    <div class="review-body">
      <h3 class="review-title">Positive: Professionalism, Quality, Value</h3>
      <p class="review-text">The team did a good job of replacing a large feature window spanning two floors, as well as the others in my property. They're a professional group who were willing to work out solutions to any problem, especially compared to other companies. Prices are fair, and my new UPVC windows look great. Special thanks to Ted for being so accommodating and for the good communication throughout.</p>
      <p class="review-service"><b>Service:</b> Window installation</p>
      <p class="review-meta">11 months ago by Martin Doyle</p>
    </div>
    <div class="review-side">
      <div class="source-name">Seekly</div>
      <div class="stars">
        <svg width="26" height="26"><use href="#star" width="26" height="26" fill="var(--gold)"/></svg><svg width="26" height="26"><use href="#star" width="26" height="26" fill="var(--gold)"/></svg><svg width="26" height="26"><use href="#star" width="26" height="26" fill="var(--gold)"/></svg><svg width="26" height="26"><use href="#star" width="26" height="26" fill="var(--gold)"/></svg><svg width="26" height="26"><use href="#star" width="26" height="26" fill="var(--gold)"/></svg>
      </div>
    </div>
  </article>

  <article class="review" style="top:423px;height:175px">
    <div class="review-body">
      <h3 class="review-title">Brilliant all round professional, friendly service.</h3>
      <p class="review-text">This home run friendly business was a real pleasure to deal with. From the professional, no pressure quote, nothing was too much trouble to ensure everything is as required for your needs with the quote and fitting. The workmanship and double glazing being fitted was brilliant and my home/outdoors was left tidy and clean leaving an outstanding impression for such an all round professional job. I would not hesitate to recommend this company, such a brilliant service from great hardworking people that care about their service.</p>
      <p class="review-meta">13 Feb 2018 by GreenChair42</p>
    </div>
    <div class="review-side">
      <div class="source-name">Localfind</div>
      <div class="stars">
        <svg width="26" height="26"><use href="#star" width="26" height="26" fill="var(--gold)"/></svg><svg width="26" height="26"><use href="#star" width="26" height="26" fill="var(--gold)"/></svg><svg width="26" height="26"><use href="#star" width="26" height="26" fill="var(--gold)"/></svg><svg width="26" height="26"><use href="#star" width="26" height="26" fill="var(--gold)"/></svg><svg width="26" height="26"><use href="#star" width="26" height="26" fill="var(--gold)"/></svg>
      </div>
    </div>
  </article>

  <article class="review" style="top:625px;height:146px">
    <div class="review-body">
      <h3 class="review-title">Front door with windows each side and side window</h3>
      <p class="review-text">This is the second time we have used regent home Upgrades , and the service is amazing! Nolan came round several times as we keep changing our minds and he was so helpful and gave us good advice, and the guys who do the fitting are efficient and tidy . I've got to say the end result is amazing and I have recommended to many of friends . Thanks Regent</p>
      <p class="review-meta">13 Feb 2018 by Jo</p>
    </div>
    <div class="review-side">
      <div class="source-name">Fairvoice</div>
      <div class="stars">
        <svg width="26" height="26"><use href="#star" width="26" height="26" fill="var(--gold)"/></svg><svg width="26" height="26"><use href="#star" width="26" height="26" fill="var(--gold)"/></svg><svg width="26" height="26"><use href="#star" width="26" height="26" fill="var(--gold)"/></svg><svg width="26" height="26"><use href="#star" width="26" height="26" fill="var(--gold)"/></svg><svg width="26" height="26"><use href="#star" width="26" height="26" fill="var(--gold)"/></svg>
      </div>
    </div>
  </article>

  <div class="load-more">Load More</div>
</main>

<footer class="powered">
  <p class="powered-label">Powered by</p>
  <div class="powered-brand"><i></i>ScoreGather</div>
</footer>
</body>
</html>
```